Hardcore nerd needs to stand out in a sea of dull Defence business cards

Wombat Devices is a new Australian consulting engineering company that turns research and theory into practical systems. No evangelistic fluff, just mathematics and physics into electronic and optical circuits for consumer products, scientific research or Defence applications.

We already have a recognised logo (provided) which is often dark blue/black on a light background but we're open to other combinations. (Us engineers tend to have limited aesthetic imagination :)

Some of our recent products have included:
* Instrumentation for electrical testing,
* Radar jammers,
* GPS antenna design,
* Satellite tracking systems,
* High power lasers

We're open to both single and double-sided designs - happy to be convinced either way.

P.S. Another group is working on the web page, so - alas - our web site is currently of no use for images/ideas...

Target Market(s)

Engineering managers,
Scientists

Contact Information for Business Card

Dr Colin Marsh
R&D Engineer

colin@wombatdevicesco.com.au
0427 563 210

PO Box XXX (to be confirmed)
Banks ACT 2913
Australia

Font styles to use
Serif
Sans Serif

Colors

Designer to choose colors to be used in the design.

Requirements
Must have
• My contact details!
• I've had many (great) "bold and plain" designs submitted already, so feel free to be artistically creative :)
• Happy to take advice re fonts/colours/printability etc.
Nice to have
• I'm not sure if "lists" are more at home on a CV than a business card, but representative services include:
• Applied electromagnetics
• RF and high speed electronics
• Signal and image processing
• Electro-optical and laser systems
• Concept-to-prototype design services
• If you're considering double sided cards, then often measuring/alignment grids/rulers feature on the back of similar cards.
• e.g. https://www.lumoptix-example.com/newgrouppage9.cfm?objectgroup_id=4815
• https://www.lumoptix-example.com/newgrouppage9.cfm?objectgroup_ID=4817
• ..or even a "Smith chart" (google will return lots)
• Generic images to represent a capability might work - googling images associated with keyword for each of these areas might help:
• - "passive radar", "phased array", "fdtd", "vircator"
• RF and high speed electronic design
• - "smith chart", "microstrip circuits", "dimensioned drawing", "electronic schematic"
• - "dft", "iir filter"
• - "optical cavity". "laser energy level diagram"
• Background/watermarked images outlines/wireframes/schematics would probably look OK.
Should not have
• If a list of projects/services is provided, it is important not to make the client feel that this is "all" the company can do. Engineering design is a creative discipline (like graphics :)
• Please, no stock "military" snaps like planes, missiles, etc!

```html
<!DOCTYPE html>
<html lang="en">
<head>
<meta charset="utf-8">
<title>Wombat Devices – Business Card</title>
<link rel="stylesheet" href="https://fonts.googleapis.com/css2?family=Open+Sans:wght@400;600;700&display=swap">
<style>
  :root {
    --stage: #e6e6e6;
    --card: #3b3b3b;
    --card-pattern: #434343;
    --silver: #c9c9c9;
    --white: #ffffff;
    --text-soft: #e4e4e4;
    --rule: #8a8a8a;
    --icon: #9a9a9a;
  }
  * { margin: 0; padding: 0; box-sizing: border-box; }
  html, body { width: 1200px; height: 800px; overflow: hidden; }
  body {
    background: var(--stage);
    font-family: "Open Sans", Arial, sans-serif;
    position: relative;
  }
  .card {
    position: absolute;
    top: 285px;
    width: 400px;
    height: 230px;
    background: var(--card);
    overflow: hidden;
  }
  .card--front { left: 160px; }
  .card--back { left: 640px; }

  .front-texture {
    position: absolute; inset: 0;
    background: radial-gradient(circle at 50% 50%, var(--card-pattern), var(--card));
  }
  .front-brand {
    position: absolute;
    left: 100px; top: 82px;
    display: flex; align-items: center; gap: 14px;
  }
  .brand-dot {
    width: 62px; height: 62px; border-radius: 50%;
    background: var(--silver);
    flex: none;
  }
  .front-brand .brand-name {
    color: var(--silver);
    font-weight: 700;
    font-size: 22px;
    line-height: 1.1;
    letter-spacing: 1px;
    text-transform: uppercase;
  }

  .back-brand {
    position: absolute;
    left: 30px; top: 26px;
    display: flex; align-items: center; gap: 10px;
  }
  .back-brand .brand-dot { width: 46px; height: 46px; background: var(--white); }
  .back-brand .brand-name {
    color: var(--white);
    font-weight: 700;
    font-size: 16px;
    line-height: 1.1;
    letter-spacing: 0.8px;
    text-transform: uppercase;
  }
  .person {
    position: absolute;
    right: 20px; top: 118px;
    text-align: right;
    color: var(--white);
  }
  .person-name { font-weight: 700; font-size: 16px; line-height: 1.2; }
  .person-role { font-size: 11px; color: var(--text-soft); margin-top: 2px; }
  .divider {
    position: absolute;
    left: 20px; right: 18px; top: 158px;
    border-top: 1px solid var(--rule);
  }
  .contact {
    position: absolute;
    left: 0; right: 0; top: 168px;
    text-align: center;
    color: var(--text-soft);
    font-size: 11px;
    line-height: 16px;
    list-style: none;
  }
  .contact li { display: block; }
  .contact-item { display: inline-flex; align-items: center; gap: 4px; margin: 0 4px; }
  .contact svg { width: 8px; height: 8px; fill: var(--icon); }
</style>
</head>
<body>
  <section class="card card--front" aria-label="Business card front">
    <div class="front-texture" role="img" aria-label="Faint repeating brand-mark pattern across the card"></div>
    <div class="front-brand">
      <span class="brand-dot"></span>
      <span class="brand-name">Wombat<br>Devices</span>
    </div>
  </section>

  <section class="card card--back" aria-label="Business card back">
    <div class="back-brand">
      <span class="brand-dot"></span>
      <span class="brand-name">Wombat<br>Devices</span>
    </div>
    <div class="person">
      <div class="person-name">Dr Colin Marsh</div>
      <div class="person-role">R&amp;D Engineer</div>
    </div>
    <div class="divider"></div>
    <ul class="contact">
      <li>
        <span class="contact-item">
          <svg viewBox="0 0 10 10"><circle cx="5" cy="5" r="5"/></svg>0427 563 210
        </span>
        <span class="contact-item">
          <svg viewBox="0 0 10 10"><circle cx="5" cy="5" r="5"/></svg>PO Box XXX
        </span>
      </li>
      <li>
        <span class="contact-item">
          <svg viewBox="0 0 10 10"><path d="M5 0a3.6 3.6 0 0 1 3.6 3.6C8.6 6.4 5 10 5 10S1.4 6.4 1.4 3.6A3.6 3.6 0 0 1 5 0z"/></svg>Banks ACT 2913, Australia
        </span>
      </li>
      <li>
        <span class="contact-item">
          <svg viewBox="0 0 10 10"><circle cx="5" cy="5" r="5"/></svg>colin@wombatdevicesco.com.au
        </span>
      </li>
    </ul>
  </section>
</body>
</html>
```